Business Card for IT company

I need a high tech looking business card using our logo. I prefer something clean and modern.

Target Market(s)

Buyers of IT hardware and software, IT Techies who are key influencers

Industry/Entity Type

Business

```html
<!DOCTYPE html>
<html lang="en">
<head>
<meta charset="utf-8">
<title>Kestrel Consulting – Business Card</title>
<link rel="stylesheet" href="https://fonts.googleapis.com/css2?family=Mulish:wght@400;700&display=swap">
<style>
  :root {
    --page: #2b2d30;
    --card-dark: #141517;
    --card-mid: #232528;
    --band: #8d8f91;
    --band-light: #a2a4a6;
    --accent: #5fc43a;
    --accent-dark: #3f9a25;
    --ink: #1a1b1c;
    --ink-soft: #4a4c4e;
    --logo: #8d8f91;
  }
  * { margin: 0; padding: 0; box-sizing: border-box; }
  html, body { width: 1200px; height: 900px; overflow: hidden; }
  body {
    background: var(--page);
    font-family: "Mulish", sans-serif;
    position: relative;
  }
  .card {
    position: absolute;
    left: 250px;
    width: 700px;
    height: 400px;
    border-radius: 22px;
    overflow: hidden;
    box-shadow: 0 10px 30px rgba(0,0,0,.45);
  }
  .card--back { top: 30px; }
  .card--front { top: 470px; }
  .card__texture {
    position: absolute; inset: 0;
    background: radial-gradient(ellipse at 60% 35%, var(--card-mid), var(--card-dark) 75%);
  }
  .card__art { position: absolute; inset: 0; width: 100%; height: 100%; }

  /* front */
  .brand {
    position: absolute;
    right: 36px; top: 56px;
    display: flex; align-items: center; gap: 12px;
    font-weight: 700; font-size: 40px; letter-spacing: 1px;
    color: var(--logo);
  }
  .brand__mark { width: 22px; height: 22px; background: var(--accent); }
  .band {
    position: absolute; left: 0; right: 0;
    background: linear-gradient(var(--band-light), var(--band));
    box-shadow: 0 2px 4px rgba(0,0,0,.5);
  }
  .band--contact { top: 200px; height: 74px; }
  .band--phone { top: 318px; height: 62px; }
  .band__tab {
    position: absolute; left: 0; top: 0; bottom: 0; width: 18px;
    background: linear-gradient(var(--accent), var(--accent-dark));
  }
  .identity {
    position: absolute; left: 26px; top: 146px;
    width: 250px; height: 92px;
    background: linear-gradient(var(--band-light), var(--band));
    box-shadow: 0 3px 6px rgba(0,0,0,.55);
    padding: 28px 0 0 40px;
  }
  .identity__name { font-weight: 700; font-size: 21px; color: var(--ink); }
  .identity__role { font-size: 13px; color: var(--ink-soft); margin-top: 6px; }
  .contact-list {
    position: absolute; list-style: none;
    font-size: 14px; color: var(--ink);
  }
  .contact-list--web { right: 40px; top: 214px; }
  .contact-list--phone { left: 110px; top: 326px; }
  .contact-list li { display: flex; align-items: center; gap: 14px; height: 24px; }
  .icon { width: 14px; height: 14px; flex: none; }
</style>
</head>
<body>

  <section class="card card--back" aria-label="Card back">
    <div class="card__texture" role="img" aria-label="Dark perforated metal texture"></div>
    <svg class="card__art" viewBox="0 0 700 400">
      <defs>
        <linearGradient id="bandFill" x1="0" y1="0" x2="0" y2="1">
          <stop offset="0" stop-color="#a2a4a6"/>
          <stop offset="1" stop-color="#85878a"/>
        </linearGradient>
      </defs>
      <polygon points="0,280 700,0 700,80 0,360" fill="url(#bandFill)"/>
      <polygon points="0,280 20,272 20,352 0,360" fill="#5fc43a"/>
      <polygon points="680,8 700,0 700,80 680,88" fill="#5fc43a"/>
      <g class="back-brand" transform="translate(440 144) rotate(-21.8)">
        <rect x="0" y="-8" width="14" height="14" fill="#5fc43a"/>
        <text x="22" y="6" font-family="Mulish, sans-serif" font-weight="700" font-size="20" fill="#2c2e30">Kestrel Consulting</text>
      </g>
    </svg>
  </section>

  <section class="card card--front" aria-label="Card front">
    <div class="card__texture" role="img" aria-label="Dark perforated metal texture"></div>

    <div class="brand"><span class="brand__mark"></span>Kestrel Consulting</div>

    <div class="band band--contact"><span class="band__tab"></span></div>
    <div class="band band--phone"><span class="band__tab"></span></div>

    <div class="identity">
      <p class="identity__name">Mara Ellison</p>
      <p class="identity__role">General manager</p>
    </div>

    <ul class="contact-list contact-list--web">
      <li>
        <svg class="icon" viewBox="0 0 14 14"><circle cx="7" cy="7" r="6" fill="none" stroke="#3f9a25" stroke-width="1.6"/><circle cx="7" cy="7" r="2.2" fill="#3f9a25"/></svg>
        ellison@kestrelconsult.com
      </li>
      <li>
        <svg class="icon" viewBox="0 0 14 14"><circle cx="7" cy="7" r="6" fill="none" stroke="#3f9a25" stroke-width="1.6"/><path d="M1 7h12M7 1v12" stroke="#3f9a25" stroke-width="1.2"/></svg>
        www.kestrelconsult.com
      </li>
    </ul>

    <ul class="contact-list contact-list--phone">
      <li>
        <svg class="icon" viewBox="0 0 14 14"><rect x="3.5" y="1" width="7" height="12" rx="1.5" fill="none" stroke="#3f9a25" stroke-width="1.5"/></svg>
        00044 555 6712
      </li>
      <li>
        <svg class="icon" viewBox="0 0 14 14"><path d="M3 1.5l2.5 2.8-1.3 1.6a7 7 0 0 0 3.9 3.9l1.6-1.3 2.8 2.5-1.6 1.6C6.5 12.6 1.4 7.5 1.4 3.1z" fill="#3f9a25"/></svg>
        0198 332 470
      </li>
    </ul>
  </section>

</body>
</html>
```